Brisk Bookings needs a New Home page

We provide online appointment scheduling. There are many schedulers out there. Ours is unique because the scheduler is shown in one compact view that can be easily incorporated into the customer's website or Chatterbay page. Whether our customer is a solo hair-stylist or a large testing center with hundreds of testing seats at multiple locations, our customer still gets the same easy-to-use, one-page scheduling experience.

Our current home page, briskbookings.example, feels cluttered and outdated. We want something more modern and minimal.

Here are web pages we like:
artmosaic.example
tillquay.example
ruvel.example

We are not unhappy with the current logo or color scheme.

Need very clear call(s) to action (i.e. sign up for trial, schedule a demo).
Design needs to look good on devices of varying size.

Here are some ideas:
“Simple Online Scheduling” - Simple, compact design, easy-to-use & powerful, time-saving, chaos-taming, affordable, one page scheduling
“Stay in touch” - Basic email confirmations, reminders or targeted email notifications for follow-ups, no shows and more
“Multiple locations? No problem” - Schedule for multiple locations on one scheduler -
“Resource Pools” - Batting cages, clerks at the DMV, computers in a lab, pilates reformer machines
“Go Social” - Scheduling for Chatterbay and mobile devices
“Visual Reporting” - Reports
“Trusted” - Testimonials, reliable since 2005, etc.
List of industries (with links to industry-specific pages)

Ultimately want to redevelop the full site.
Updates

Reason: Please do not submit any new designs. We are now just wrapping up polling and discussing details. Thank you to all designers who have submitted. We feel lucky to get to chose from many great designs.

Target Market(s)

Audience is very broad including solo entrepreneurs (massage therapist, accountants, lawyers), educational institutions (elementary schools, university departments, advisers, testing centers), health care providers and screening services, to government.

Industry/Entity Type

Online

Requirements
Must have
• Call(s) to action, i.e. sign up for trial, schedule a demo.
• Look good on devices of different sizes.

```html
<!DOCTYPE html>
<html lang="en">
<head>
<meta charset="utf-8">
<title>Brisk Bookings – Simple Online Scheduling</title>
<link href="https://fonts.googleapis.com/css2?family=Dosis:wght@300;400;500&family=Open+Sans:wght@400;600&display=swap" rel="stylesheet">
<style>
:root{
  --ink-dark:#2a2a2a;
  --ink-darker:#232323;
  --coral:#f25b55;
  --coral-deep:#e94e48;
  --paper:#ffffff;
  --mist:#ececec;
  --text:#333333;
  --muted:#9a9a9a;
  --rule:#3d3d3d;
}
*{margin:0;padding:0;box-sizing:border-box}
html,body{width:784px;height:1200px;overflow:hidden;background:var(--paper)}
body{font-family:"Open Sans",sans-serif;color:var(--text);position:relative}
.abs{position:absolute}

/* header */
.site-header{left:0;top:0;width:784px;height:88px;background:var(--ink-dark);border-bottom:1px solid var(--rule)}
.brand{left:86px;top:16px;font-family:"Dosis",sans-serif;font-weight:400;font-size:22px;letter-spacing:4px;color:#f0f0f0}
.brand span{color:#f0f0f0}
.util-links{right:86px;top:24px;font-size:7.5px;color:#bbb}
.util-links i{font-style:normal;margin:0 5px}
.nav-rule{left:0;top:56px;width:784px;height:1px;background:var(--rule)}
.nav-active{left:86px;top:56px;width:32px;height:2px;background:var(--coral)}
.main-nav{left:91px;top:68px;display:flex;gap:24px;font-size:7.5px;color:#e6e6e6;text-transform:uppercase}

/* hero */
.hero{left:0;top:88px;width:784px;height:282px;background:var(--ink-dark)}
.hero-title{left:100px;top:112px;font-family:"Dosis",sans-serif;font-weight:300;font-size:22px;color:#eee}
.benefits{left:100px;top:158px;list-style:none;font-family:"Dosis",sans-serif;font-weight:300;font-size:13px;color:#ddd}
.benefits li{height:24.5px;display:flex;align-items:center;gap:7px}
.benefits svg{width:9px;height:9px}
.product-shot{left:394px;top:120px}
.slide-dots{left:378px;top:354px;display:flex;gap:5px}
.slide-dots b{width:6px;height:6px;border-radius:50%;border:1px solid #888;background:#555}

/* proof band */
.proof-band{left:0;top:370px;width:784px;height:96px;background:var(--coral)}
.proof-divider{left:475px;top:370px;width:1px;height:96px;background:var(--coral-deep)}
.proof-title{left:86px;top:379px;font-size:12.5px;color:#fff}
.partner-badge{left:86px;top:403px;width:127px;height:50px;background:#fff}
.partner-badge div{position:absolute;left:10px;top:17px;font-size:11px;font-weight:600;color:#2a5fa8}
.proof-copy{left:221px;top:401px;width:235px;font-size:7.2px;line-height:11.6px;color:#fff}
.proof-copy p+p{margin-top:5px}
.cta-trial{left:521px;top:394px;width:177px;height:45px;background:var(--ink-darker);color:#fff;font-size:15.5px;display:flex;align-items:center;justify-content:center}

/* value cards */
.values{left:0;top:466px;width:784px;height:146px;background:var(--mist)}
.value-card{top:481px;width:196px;height:115px;background:#fff;text-align:center;padding:7px 10px 0}
.value-card h3{font-weight:400;font-size:13px;color:#333}
.value-card .quote{font-size:7.8px;line-height:10.5px;color:var(--coral);margin-top:7px}
.value-card .lead{font-size:8px;color:#444;margin-top:11px}
.value-card .note{font-size:7.3px;line-height:10.5px;color:#444;margin-top:10px}

/* email section */
.feature-title{left:86px;top:621px;font-size:13px;color:#333}
.feature-copy{left:86px;top:645px;width:296px;font-size:7.2px;line-height:11.6px;color:#333}
.feature-copy p{margin-bottom:7px}
.report-shot{left:397px;top:638px}
.tagline{left:0;top:860px;width:784px;text-align:center;font-size:13.5px;color:var(--coral)}

/* pillars */
.pillars{left:0;top:887px;width:784px;height:123px;background:var(--coral)}
.pillar-divider{top:887px;width:1px;height:123px;background:var(--coral-deep)}
.pillar{top:896px;width:198px;color:#fff;font-size:7.2px;line-height:10.4px}
.pillar h4{font-weight:400;font-size:11px;margin-bottom:5px}
.pillar p{margin-bottom:7px}

/* industries */
.industries-title{left:0;top:1019px;width:784px;text-align:center;font-size:13px;color:#333}
.industries-rule{left:0;top:1041px;width:784px;height:1px;background:#ddd}
.industry{display:flex;align-items:center;gap:9px;font-size:9.5px;color:#333}
.industry svg{width:36px;height:36px}

/* footer */
.site-footer{left:0;top:1158px;width:784px;height:42px;background:var(--ink-dark)}
.legal{left:86px;top:1174px;font-size:7px;color:#aaa}
.legal i{font-style:normal;margin:0 6px}
.social{right:86px;top:1173px;font-size:8.5px;font-weight:600;color:#fff}
</style>
</head>
<body>

<header class="abs site-header"></header>
<div class="abs brand">BRISK <span>BOOKINGS</span></div>
<div class="abs util-links">Now Scheduling on your CHATTERBAY Page<i>|</i>Account Login</div>
<div class="abs nav-rule"></div>
<div class="abs nav-active"></div>
<nav class="abs main-nav">
  <span>Home</span><span>See it work</span><span>Who it's for</span><span>Our scheduler</span><span>Free trail</span><span>Dig in</span><span>About us</span><span>Contact us</span>
</nav>

<section class="abs hero"></section>
<h1 class="abs hero-title">Simple Online Scheduling</h1>
<ul class="abs benefits">
  <li><svg viewBox="0 0 10 10"><rect width="10" height="10" fill="#eee"/><path d="M2 5l2 2 4-4.5" stroke="#2a2a2a" stroke-width="1.6" fill="none"/></svg>Simple</li>
  <li><svg viewBox="0 0 10 10"><rect width="10" height="10" fill="#eee"/><path d="M2 5l2 2 4-4.5" stroke="#2a2a2a" stroke-width="1.6" fill="none"/></svg>Compact Design</li>
  <li><svg viewBox="0 0 10 10"><rect width="10" height="10" fill="#eee"/><path d="M2 5l2 2 4-4.5" stroke="#2a2a2a" stroke-width="1.6" fill="none"/></svg>Easy-to-use &amp; powerful</li>
  <li><svg viewBox="0 0 10 10"><rect width="10" height="10" fill="#eee"/><path d="M2 5l2 2 4-4.5" stroke="#2a2a2a" stroke-width="1.6" fill="none"/></svg>Time-saving</li>
  <li><svg viewBox="0 0 10 10"><rect width="10" height="10" fill="#eee"/><path d="M2 5l2 2 4-4.5" stroke="#2a2a2a" stroke-width="1.6" fill="none"/></svg>Chaos-taming</li>
  <li><svg viewBox="0 0 10 10"><rect width="10" height="10" fill="#eee"/><path d="M2 5l2 2 4-4.5" stroke="#2a2a2a" stroke-width="1.6" fill="none"/></svg>Affordable</li>
  <li><svg viewBox="0 0 10 10"><rect width="10" height="10" fill="#eee"/><path d="M2 5l2 2 4-4.5" stroke="#2a2a2a" stroke-width="1.6" fill="none"/></svg>One page scheduling</li>
</ul>
<svg class="abs product-shot" width="304" height="242" viewBox="0 0 304 242" role="img" aria-label="Desktop monitor showing the one-page appointment scheduler">
  <rect x="0" y="0" width="304" height="210" rx="6" fill="#111"/>
  <rect x="12" y="10" width="280" height="164" fill="#f4f4f4"/>
  <rect x="12" y="10" width="280" height="20" fill="#dfe3ea"/>
  <rect x="0" y="182" width="304" height="28" rx="4" fill="#d9d9d9"/>
  <path d="M118 210h68l8 28h-84z" fill="#c4c4c4"/>
  <rect x="104" y="236" width="96" height="6" rx="3" fill="#aaa"/>
</svg>
<div class="abs slide-dots"><b></b><b></b><b></b></div>

<section class="abs proof-band"></section>
<div class="abs proof-divider"></div>
<h2 class="abs proof-title" style="font-weight:400">2,000,000+ SOLA appointments!</h2>
<div class="abs partner-badge"><div>Sunstate Online Academy</div></div>
<div class="abs proof-copy">
  <p>Students schedule time with teachers using Brisk Bookings. We are proud to aid in the vision of SOLA to provide world-class education</p>
  <p>Read more...</p>
</div>
<a class="abs cta-trial">30 Days FREE Trial</a>

<section class="abs values"></section>
<article class="abs value-card" style="left:86px">
  <h3>Save time</h3>
  <p class="quote">Teach Forward Corps saves "considerable man hours..."</p>
  <p class="lead">You can too!</p>
  <p class="note">Clients will love the convenience. So will you and your staff.</p>
</article>
<article class="abs value-card" style="left:294px">
  <h3>Simplify...</h3>
  <p class="quote">Kahili Wellness has "eliminated missed or mixed-up appointments"</p>
  <p class="lead">Sign up. Begin scheduling today.</p>
  <p class="note">Greater flexibility and scalability mean you can start now and grow later.</p>
</article>
<article class="abs value-card" style="left:502px">
  <h3>It's affordable!</h3>
  <p class="quote">For Stillwater Massage it's "one of the best investments..."</p>
  <p class="lead">It is easy to try before you buy.</p>
  <p class="note">Take advantage of our unmatched pricing, built for your budget.</p>
</article>

<h2 class="abs feature-title" style="font-weight:400">Targeted Email Notifications</h2>
<div class="abs feature-copy">
  <p>Get the right information to the right person at the right time!</p>
  <p>Do you want to stay in touch with your clients? Want to set expectations and keep clients informed before an appointment? Would you like to follow up with a thank you or survey afterward? Or remind them to schedule their next appointment at the right time? Do you want to check in with clients who didn't show up?</p>
  <p>Yes? Then, our targeted email notifications are for you! You control the timing and content of the email. Yet the system sends them out automatically. Just create a template, optionally tied to specific service, timed to go out when it makes the most sense relative to the appointment.</p>
  <p>Dentists can automatically remind patients to schedule their next cleaning 5 months after the last cleaning. They can follow up with a patient who just had a root canal to ask how the patient is doing.</p>
  <p>Testing centers can inform students what to bring for each given test.</p>
  <p>Try it. It is free until this Halloween!</p>
</div>
<svg class="abs report-shot" width="301" height="199" viewBox="0 0 301 199" role="img" aria-label="Reporting dashboard with a pie chart of time spent by section">
  <rect width="301" height="199" fill="#2c3039"/>
  <rect x="10" y="10" width="281" height="189" fill="#f7f7f7"/>
  <rect x="10" y="10" width="281" height="12" fill="#3a3f4a"/>
  <circle cx="112" cy="125" r="30" fill="#c06be0"/>
  <path d="M112 125L142 125A30 30 0 0 1 112 155Z" fill="#7fcf9a"/>
  <path d="M112 125L112 155A30 30 0 0 1 84 135Z" fill="#f2dc6a"/>
  <path d="M112 125L84 135A30 30 0 0 1 86 110Z" fill="#4aa3df"/>
  <rect x="223" y="30" width="62" height="160" fill="#ececec"/>
</svg>
<p class="abs tagline">Multiple location scheduling is a breeze... as always... like nobody else!</p>

<section class="abs pillars"></section>
<div class="abs pillar-divider" style="left:290px"></div>
<div class="abs pillar-divider" style="left:494px"></div>
<div class="abs pillar" style="left:86px">
  <h4>Affordable</h4>
  <p>Online appointment scheduling starts at just 10/month with the Solo Plan. All plans offer</p>
  <p>Unlimited appointments &amp; Unlimited Users</p>
  <p>No sneaky charges for high appointment scheduling volume or additional logins.</p>
</div>
<div class="abs pillar" style="left:296px">
  <h4>Easy to Use</h4>
  <p>Our appointment scheduler is a rich internet application (RIA). Updates occur quickly on a single compact page making it easy for clients to shop for an ideal opening.</p>
  <p>That is important, especially when your appointment calendar is filling up and availability is limited.</p>
</div>
<div class="abs pillar" style="left:500px">
  <h4>Powerful</h4>
  <p>The online appointment scheduler scales up to meet your growing business needs. Try our online scheduling demos to see how we can handle</p>
  <p style="margin-bottom:4px">Many schedules,</p>
  <p style="margin-bottom:4px">Complex service menus,</p>
  <p>Multiple locations</p>
</div>

<h2 class="abs industries-title" style="font-weight:400">Currently scheduling online appointments for</h2>
<div class="abs industries-rule"></div>
<div class="abs industry" style="left:86px;top:1054px"><svg viewBox="0 0 36 36"><circle cx="18" cy="18" r="16.5" fill="#fff" stroke="#333" stroke-width="2"/><text x="18" y="22" text-anchor="middle" font-size="11" font-weight="600" font-family="Open Sans,sans-serif" fill="#222">+/=</text></svg>Accounts</div>
<div class="abs industry" style="left:239px;top:1054px"><svg viewBox="0 0 36 36" role="img" aria-label="Education icon"><circle cx="18" cy="18" r="16.5" fill="#fff" stroke="#333" stroke-width="2"/><circle cx="18" cy="18" r="11" fill="#222"/></svg>Education</div>
<div class="abs industry" style="left:392px;top:1054px"><svg viewBox="0 0 36 36" role="img" aria-label="Health icon"><circle cx="18" cy="18" r="16.5" fill="#fff" stroke="#333" stroke-width="2"/><rect x="11" y="9" width="14" height="18" fill="#e05a4a"/><path d="M18 13v10M13 18h10" stroke="#fff" stroke-width="2.5"/></svg>Health</div>
<div class="abs industry" style="left:545px;top:1054px"><svg viewBox="0 0 36 36" role="img" aria-label="Massage icon"><circle cx="18" cy="18" r="16.5" fill="#fff" stroke="#333" stroke-width="2"/><circle cx="18" cy="18" r="11" fill="#3a74b8"/></svg>Massage</div>
<div class="abs industry" style="left:86px;top:1102px"><svg viewBox="0 0 36 36" role="img" aria-label="Salon photo"><circle cx="18" cy="18" r="16.5" fill="#e9c9b3" stroke="#333" stroke-width="2"/></svg>Salon</div>
<div class="abs industry" style="left:239px;top:1102px"><svg viewBox="0 0 36 36" role="img" aria-label="Spa stones photo"><circle cx="18" cy="18" r="16.5" fill="#cfcfcf" stroke="#333" stroke-width="2"/></svg>Spa</div>
<div class="abs industry" style="left:392px;top:1102px"><svg viewBox="0 0 36 36" role="img" aria-label="Tax calculator icon"><circle cx="18" cy="18" r="16.5" fill="#fff" stroke="#333" stroke-width="2"/><rect x="11" y="9" width="14" height="18" rx="2" fill="#333"/><rect x="13" y="11" width="10" height="4" fill="#cde"/></svg>Tax</div>
<div class="abs industry" style="left:545px;top:1102px"><svg viewBox="0 0 36 36" role="img" aria-label="Wellness martial arts uniform icon"><circle cx="18" cy="18" r="16.5" fill="#fff" stroke="#333" stroke-width="2"/><circle cx="18" cy="18" r="11" fill="#222"/></svg>Wellness</div>

<footer class="abs site-footer"></footer>
<div class="abs legal">© 2013 Brisk Bookings. All rights reserved<i>|</i>Privacy &amp; Billing Policies<i>|</i>Terms &amp; Conditions</div>
<div class="abs social">chatterbay</div>

</body>
</html>
```